Motivational Poster Design Project

I would like to create a poster with some of my favorite quotes to hang in my office.

Industry/Entity Type

Quotes

Requirements
Must have
• The poster will be 24" high x 36" long and printed on canvas, so the image you create needs to have a resolution of at least 2700 x 3900.

The poster must contain the following quotes:

“Your beliefs become your thoughts,
Your thoughts become your words,
Your words become your actions,
Your actions become your habits,
Your habits become your values,
Your values become your destiny.”
-Varuna Pellath

"Winners practice until they get it right. Champions practice until they can’t get it wrong!"
-Unknown

"Style is the perfection of a point of view."
-Conrad Whitlowe

"My interest in life comes from setting myself huge, apparently unachieveable challenges and trying to rise above them."
-Sir Oswin Talbrook

"Problems cannot be solved by the same level of thinking that created them."
-Gustav Morrendel

"People think focus means saying yes to the thing you've got to focus on. But that's not what it means at all. It means saying no to the hundred other good ideas that there are. You have to pick carefully."
-Dale Parrick

"Think like a man of action and act like a man of thought."
-Lucien Marvaud
Nice to have
• It would be nice to have an image of each person who is being quoted (if known) along with the quote that is attributable to them.

```html
<!DOCTYPE html>
<html lang="en">
<head>
<meta charset="utf-8">
<title>Quotes Poster</title>
<link rel="stylesheet" href="https://fonts.googleapis.com/css2?family=Marcellus+SC&family=Kaushan+Script&display=swap">
<style>
  :root {
    --bg-deep: #0f1a17;
    --bg-mid: #1f3a31;
    --bg-glow: #4c6e4a;
    --bg-warm: #7a7a3e;
    --ink: #f2f4ea;
    --portrait-light: #b9c2a6;
    --portrait-mid: #6d7d68;
    --portrait-dark: #1c2b25;
  }
  html, body {
    margin: 0;
    padding: 0;
    width: 800px;
    height: 1200px;
    overflow: hidden;
    background: var(--bg-deep);
  }
  .poster {
    position: relative;
    width: 800px;
    height: 1200px;
    overflow: hidden;
    background:
      radial-gradient(ellipse 380px 260px at 520px 120px, rgba(90,140,110,.55), transparent 70%),
      radial-gradient(ellipse 420px 300px at 420px 600px, rgba(110,140,90,.45), transparent 72%),
      radial-gradient(ellipse 420px 320px at 600px 1050px, rgba(140,140,60,.55), transparent 70%),
      radial-gradient(ellipse 300px 260px at 180px 420px, rgba(80,130,100,.35), transparent 70%),
      linear-gradient(160deg, var(--bg-mid) 0%, var(--bg-deep) 45%, var(--bg-mid) 70%, #2c3a22 100%);
    font-family: "Marcellus SC", "Times New Roman", serif;
    color: var(--ink);
  }
  .portrait {
    position: absolute;
    border-radius: 50%;
    background: radial-gradient(ellipse at 50% 45%, var(--portrait-light) 0%, var(--portrait-mid) 40%, rgba(28,43,37,.6) 65%, transparent 80%);
  }
  .portrait--vivid {
    background: radial-gradient(ellipse at 50% 45%, #d3c9b0 0%, #8a8d72 40%, rgba(28,43,37,.6) 65%, transparent 80%);
  }
  .quote {
    position: absolute;
    margin: 0;
    text-align: center;
    font-size: 17px;
    line-height: 22px;
    letter-spacing: .3px;
    text-shadow: 0 0 4px rgba(0,0,0,.6);
  }
  .author {
    position: absolute;
    margin: 0;
    font-family: "Kaushan Script", cursive;
    font-size: 25px;
    line-height: 30px;
    white-space: nowrap;
    text-shadow: 0 0 4px rgba(0,0,0,.6);
  }
</style>
</head>
<body>
<main class="poster">

  <div class="portrait" style="left:150px;top:62px;width:150px;height:165px" role="img" aria-label="Portrait of Varuna Pellath"></div>
  <p class="quote" style="left:300px;top:72px;width:440px;line-height:23px">“Your beliefs become your thoughts,<br>Your thoughts become your words,<br>Your words become your actions,<br>Your actions become your habits,<br>Your habits become your values,<br>Your values become your destiny.”</p>
  <p class="author" style="left:465px;top:236px">-Varuna Pellath</p>

  <div class="portrait" style="left:380px;top:280px;width:185px;height:200px" role="img" aria-label="Portrait of Dale Parrick"></div>
  <p class="quote" style="left:30px;top:268px;width:400px">“People think focus means<br>saying yes to the thing you’ve<br>got to focus on. But that’s not<br>what it means at all. It means<br>saying no to the hundred<br>other good ideas that there<br>are. You have to pick carefully.”</p>
  <p class="author" style="left:160px;top:462px">-Dale Parrick</p>

  <p class="quote" style="left:555px;top:284px;width:200px;font-size:16px">“Winners practice<br>until they get it<br>right. Champions<br>practice until they<br>can’t get it wrong!”</p>
  <p class="author" style="left:577px;top:428px">-Unknown</p>

  <div class="portrait" style="left:205px;top:485px;width:135px;height:150px" role="img" aria-label="Portrait of Conrad Whitlowe"></div>
  <p class="quote" style="left:345px;top:548px;width:340px">“Style is the perfection of a<br>point of view.”</p>
  <p class="author" style="left:393px;top:603px">-Conrad Whitlowe</p>

  <div class="portrait" style="left:495px;top:650px;width:180px;height:180px" role="img" aria-label="Portrait of Lucien Marvaud"></div>
  <p class="quote" style="left:70px;top:705px;width:380px">“Think like a man of action and<br>act like a man of thought.”</p>
  <p class="author" style="left:170px;top:766px">-Lucien Marvaud</p>

  <div class="portrait portrait--vivid" style="left:85px;top:805px;width:180px;height:180px" role="img" aria-label="Portrait of Sir Oswin Talbrook"></div>
  <p class="quote" style="left:255px;top:840px;width:370px">“My interest in life comes from<br>setting myself huge, apparently<br>unachieveable challenges and<br>trying to rise above them.”</p>
  <p class="author" style="left:383px;top:945px">-Sir Oswin Talbrook</p>

  <div class="portrait" style="left:505px;top:975px;width:180px;height:165px" role="img" aria-label="Portrait of Gustav Morrendel"></div>
  <p class="quote" style="left:140px;top:980px;width:365px">“Problems cannot be solved by<br>the same level of thinking<br>that created them.”</p>
  <p class="author" style="left:225px;top:1078px">-Gustav Morrendel</p>

</main>
</body>
</html>
```